Stationary, memo and report templates for professional services company

Looking for someone to update stationary design but just as importantly come up with a template for reports and memos for use in our consulting firm. Would also like some brand use guidelines to be able to share with our whole team. We have an existing logo that we like. Need to update with a more contemporary look so that our deliverables to clients look good and professional yet stylish. This is for business to business communications. No need for envelope design. Important to have design for multiple pages, i.e. first page of a report and then 2nd page. Need to use in MS word documents so must be easy to use and replicate. Don't want something overly complex. Clean, fresh looking is best.

Target Market(s)

Business to business; non-profit cultural attractions

Colors

Designer to choose colors to be used in the design.

Requirements
Must have
• Clean look but with a little style or pop. Something that can easily be used in word documents. Need to have page styles that have a first page of a report (not a cover page) and then secondary page.
Nice to have
• Although the dark blue is our primary color. Might be willing to look at some accent color as well.
Should not have
• Not just our logo on the page with a color bar.

```html
<!DOCTYPE html>
<html lang="en">
<head>
<meta charset="utf-8">
<title>Kestrel Advisors – Report Templates</title>
<link href="https://fonts.googleapis.com/css2?family=Open+Sans:wght@400;600;700&display=swap" rel="stylesheet">
<style>
:root{
  --navy:#1f3a7a;
  --navy-deep:#1a2f68;
  --navy-light:#2c4c92;
  --ink:#333a45;
  --muted:#6b7280;
  --rule:#8da3c9;
  --tint:#d6e6f5;
  --tint-2:#e9f1fa;
  --stage:#b3b3b3;
  --orange:#f58220;
  --gold:#f5b800;
  --sky:#3d8bd6;
  --grey:#a6a6a6;
}
*{box-sizing:border-box;margin:0;padding:0}
html,body{width:1200px;height:1200px;overflow:hidden}
body{background:var(--stage);font-family:"Open Sans",sans-serif;color:var(--ink);position:relative}
.page{position:absolute;width:269px;height:348px;background:#fff;box-shadow:2px 3px 6px rgba(0,0,0,.25);overflow:hidden}
.c1{left:29px}.c2{left:322px}.c3{left:618px}.c4{left:908px}
.r1{top:40px}.r2{top:414px}.r3{top:792px}
.page-title{position:absolute;top:24px;left:26px;right:26px;text-align:center;font-size:9px;font-weight:600;color:var(--ink);letter-spacing:.2px;padding-bottom:3px;border-bottom:1px solid var(--rule)}
.page-title b{color:var(--navy);font-weight:700}
.body{position:absolute;left:26px;right:26px;top:46px}
.tx{font-size:4.1px;line-height:1.55;color:var(--ink);margin-bottom:5px}
.tx.c{text-align:center}
.tx a{color:var(--navy)}
.sub{font-size:4.3px;font-style:italic;color:var(--muted);margin:4px 0 2px}
.h3{font-size:7.2px;font-weight:600;color:var(--ink);margin:6px 0 2px}
.foot{position:absolute;left:0;right:0;bottom:0;height:15px;background:var(--navy)}
.foot .mark{position:absolute;left:20px;top:3px;font-size:5px;font-weight:700;color:#fff;letter-spacing:.4px}
.foot .num{position:absolute;right:20px;top:4px;font-size:4.5px;color:#fff}
/* cover */
.cover-title{position:absolute;left:36px;top:40px;border-left:5px solid #555;padding-left:10px;height:88px}
.cover-title h1{font-size:15px;line-height:1.35;font-weight:700;color:var(--navy)}
.cover-title h1 span{color:#4a4a4a}
.cover-title p{font-size:6px;color:#666;margin-top:26px;line-height:1.6}
.cover-meta{position:absolute;left:34px;top:214px;font-size:6.5px;color:var(--navy);line-height:1.8}
.cover-band{position:absolute;left:0;right:0;bottom:0;height:98px;background:var(--navy)}
.cover-band svg{position:absolute;left:0;top:0}
.brand-big{position:absolute;right:28px;bottom:16px;font-size:18px;font-weight:600;color:#fff;letter-spacing:1.2px;line-height:1.1;text-align:right}
/* version table */
table{border-collapse:collapse;width:100%}
.ver{position:absolute;left:36px;top:46px;width:226px}
.ver td,.ver th{border:.5px solid #ccc;height:10px;font-size:4px;font-weight:400;color:var(--navy);text-align:left;padding-left:2px}
.ver th{background:#ececec}
.ver td:nth-child(2){background:#ececec}
.copy{position:absolute;left:72px;top:305px;border-left:2px solid var(--navy);padding-left:6px;font-size:3.2px;line-height:1.6;color:#444;width:160px}
/* toc */
.toc{list-style:none;position:absolute;left:26px;right:30px;top:52px}
.toc li{display:flex;font-size:4.1px;line-height:2.15;color:var(--ink)}
.toc li span.d{flex:1;border-bottom:.6px dotted #888;margin:0 3px 2px}
.toc li.gap{margin-top:5px}
/* chart page */
.lead{font-size:5.6px;font-weight:700;color:var(--navy);text-align:center;line-height:1.35}
.chart-title{font-size:7px;text-align:center;color:#222;margin-top:10px;line-height:1.3}
.legend{display:flex;justify-content:center;gap:5px;font-size:3.4px;color:#555;margin-top:2px}
.legend i{display:inline-block;width:3px;height:3px;margin-right:1px}
.just{text-align:justify}
/* data tables */
.grid td{border:.6px solid #7f9ccf;height:10px;background:#fff}
.grid tr:first-child td{background:var(--navy);height:7px}
.grid tr:nth-child(even) td{background:var(--tint-2)}
.grid.light tr:first-child td{background:var(--tint-2);height:10px}
.est{border-spacing:2px 1.5px;border-collapse:separate}
.est th{background:var(--navy);color:#fff;font-size:4px;font-weight:600;height:7px}
.est td{background:var(--tint);font-size:3.8px;height:7px;padding-left:4px;color:var(--navy)}
.est td.n{text-align:center;padding:0}
.est tr.ph td{background:#fff;font-weight:600;font-size:4.4px}
.est tr.tot td{background:#d9d9d9;font-weight:600;color:#222}
.est tr.grand td{background:var(--tint);font-weight:600}
.est tr.grand td.n{background:#9cc3ea}
/* photo page */
.photo{position:absolute;left:29px;top:45px;width:210px;height:94px;background:linear-gradient(135deg,#8b5a3c,#c9a27a 45%,#5a6d8a)}
.mission{font-size:5.8px;font-weight:700;color:var(--navy);line-height:1.25;margin-bottom:6px}
.bar{height:10px;background:var(--tint);margin:4px 0 8px}
/* back cover */
.back-band{position:absolute;left:0;top:0;right:0;height:250px;background:var(--navy)}
.back-brand{position:absolute;top:272px;left:0;right:0;text-align:center;font-size:10px;font-weight:600;color:var(--navy);letter-spacing:.8px}
.contacts{position:absolute;top:307px;left:52px;display:flex;font-size:4px;color:var(--navy);line-height:1.9}
.contacts div{padding:0 8px;border-left:.8px solid var(--navy)}
.contacts div:first-child{border:0;padding-left:0}
</style>
</head>
<body>

<section class="page c1 r1">
  <div class="cover-title">
    <h1>LOREM IPSUM IS SIMPLY<br><span>DUMMY HAS BEEN</span></h1>
    <p>LOREM IPSUM IS SIMPLY ETIAM VESTIBULUM<br>Lorem ipsum is simply</p>
  </div>
  <div class="cover-meta">Lorem Ipsum Is Simply Etiam<br>Lorem Ipsum Is</div>
  <div class="cover-band">
    <svg width="269" height="98" aria-hidden="true"><polygon points="40,0 110,0 75,98" fill="var(--navy-light)"/><polygon points="110,0 269,0 269,60" fill="var(--navy-deep)" opacity=".5"/></svg>
    <div class="brand-big">KESTREL<br>ADVISORS</div>
  </div>
</section>

<section class="page c2 r1">
  <table class="ver">
    <tr><th>Version #</th><th>Purpose / Changes</th><th>Author</th><th>Date</th></tr>
    <tr><td></td><td></td><td></td><td></td></tr>
    <tr><td></td><td></td><td></td><td></td></tr>
    <tr><td></td><td></td><td></td><td></td></tr>
    <tr><td></td><td></td><td></td><td></td></tr>
    <tr><td></td><td></td><td></td><td></td></tr>
    <tr><td></td><td></td><td></td><td></td></tr>
    <tr><td></td><td></td><td></td><td></td></tr>
  </table>
  <div class="copy">Copyright © 2018 Kestrel Group.<br>All Rights Reserved.<br>No part of the contents of this document may be reproduced or distributed in any form or by any means without the prior written permission of Kestrel Group.</div>
</section>

<section class="page c3 r1">
  <h2 class="page-title">TABLE OF <b>CONTENTS</b></h2>
  <ul class="toc">
    <li>Table of Contents<span class="d"></span>01</li>
    <li>Executive Summary<span class="d"></span>02</li>
    <li>Our Understanding of Your Needs<span class="d"></span>02</li>
    <li>Our Recommendations<span class="d"></span>03</li>
    <li>Our Approach<span class="d"></span>05</li>
    <li>Budget and Timeframe<span class="d"></span>07</li>
    <li>Appendix A: About Our Firm<span class="d"></span>10</li>
    <li>Appendix B: Selected Client List<span class="d"></span>10</li>
    <li>Appendix C: Our Capabilities<span class="d"></span>11</li>
    <li>Appendix D: Our Process<span class="d"></span>12</li>
    <li class="gap">Table of Contents<span class="d"></span>01</li>
    <li>Executive Summary<span class="d"></span>02</li>
    <li>Our Understanding of Your Needs<span class="d"></span>02</li>
    <li>Our Recommendations<span class="d"></span>03</li>
    <li>Our Approach<span class="d"></span>05</li>
    <li>Budget and Timeframe<span class="d"></span>07</li>
    <li>Appendix A: About Our Firm<span class="d"></span>10</li>
    <li>Appendix B: Selected Client List<span class="d"></span>10</li>
    <li>Appendix C: Our Capabilities<span class="d"></span>11</li>
    <li>Appendix D: Our Process<span class="d"></span>12</li>
  </ul>
  <footer class="foot"><span class="mark">KESTREL</span><span class="num">1</span></footer>
</section>

<section class="page c4 r1">
  <h2 class="page-title">PUT HEADLINE <b>CONTENTS</b></h2>
  <div class="body">
    <p class="tx">Administrative tasks are cumbersome, time-consuming and often prevent small owners from focusing their time and energy on their business and their customers. They can also be extremely stressful for those attempting these tasks for the first time.</p>
    <p class="tx c">At Ledgerly, we envisage accounting for the self-employed and small business owners as being <a>automated and decentralized</a></p>
    <p class="tx">Accounting can and should be done automatically. By connecting to all sources of accounting data such as bank accounts, payment systems and invoicing systems, Ledgerly automatically completes these tasks, which would take hours to do manually. Statements are available within a couple of clicks.</p>
    <p class="tx">What may seem like a pipedream to the millions of self-employed who struggle with their admin, is already a reality. Now is the time to join Ledgerly on its mission to transform bookkeeping.</p>
    <h3 class="h3">The Ledgerly model</h3>
    <p class="tx">Ledgerly is based on an innovative license model that uses Token-as-a-License (TaaL). The token represents lifelong software license for Ledgerly solutions. The token sales will enable Ledgerly to complete its development of fully automatic bookkeeping.</p>
    <p class="tx">The token sale will also pave the way for a future Ledgerly offering. Ledgerly will launch accounting on the blockchain and ensure your accounting data is comprehensive and private, but available everywhere within your preferred apps. Furthermore, a new range of business apps will connect to Ledgerly to provide you with leading edge business data access.</p>
    <p class="tx">Ledgerly supports strong data ownership laws that truly protect individuals and ensure they have complete ownership of their data, to decide how it should be used.</p>
    <p class="tx">To find out more about the project, please register with your email at <a>www.ledgerly.example</a> so we can notify you about our upcoming purchase periods.</p>
  </div>
  <footer class="foot"><span class="mark">KESTREL</span><span class="num">3</span></footer>
</section>

<section class="page c1 r2">
  <h2 class="page-title">PUT HEADLINE <b>CONTENTS</b></h2>
  <div class="body">
    <h3 class="h3" style="margin-top:0">Solution</h3>
    <p class="sub">AI automated accounting</p>
    <p class="tx">Ledgerly builds automation in stages on top of its current system to reach full automation thanks to the Ledgerly AI. It automates every manual task performed by the user, starting by connecting to all sources of accounting data such as bank accounts, credit cards, webshops or document management systems. Based on these data, it creates bookings and generates financial reports. Finally, a chat-like interface allows users to communicate seamlessly with it, viewing it as a trusted advisor over time for all their accounting queries.</p>
    <p class="sub">Blockchain software license or Token-as-a-License (TaaL)</p>
    <p class="tx">It is possible to create tokens on blockchain that represent software licenses, also known as Token-as-a-Licence. Ledgerly creates TaaL by using the Corvid official wallet which interacts with the Corvid blockchain. Upon purchase, the token holder is free to transfer or sell it using a secondary market that is built directly over the blockchain. Ledgerly checks the validity of a token against the blockchain ensuring that token holders have access to the software. TaaL makes distribution and resale easier for developers and for owners.</p>
    <h3 class="h3">Pre-ICO Token sale</h3>
    <p class="tx">To realize this innovative vision, Ledgerly is launching a pre-sale of a token on the Corvid blockchain. 20,000,000 tokens are available to purchase for the price of CHF 0.10 each during a 30-day period to be announced. Tokens represent lifelong software licenses. Future customers will still have the opportunity to buy directly yearly or monthly subscriptions.</p>
    <h3 class="h3">Future plans</h3>
    <p class="tx">A future offering is planned between 18 and 24 months after the pre-sale. This offering will support the development of Ledgerly into a fully decentralized, privacy-focused ecosystem of applications. The new model will reward each participant.</p>
  </div>
  <footer class="foot"><span class="mark">KESTREL</span><span class="num">2</span></footer>
</section>

<section class="page c2 r2">
  <h2 class="page-title">PUT HEADLINE <b>CONTENTS</b></h2>
  <div class="body">
    <p class="lead">Lorem ipsum dolor sit amet, consectetur adipisicing do eiusmod tempor incididunt ut labore et dolore magna aliqua. Ut enim ad minim veniam,</p>
    <p class="chart-title">USE OF FOUNDER SEED CAPITAL<br>$1.12M SINCE JAN 2014</p>
    <div class="legend"><span><i style="background:var(--sky)"></i>marketing</span><span><i style="background:var(--orange)"></i>sg&amp;a</span><span><i style="background:var(--grey)"></i>r&amp;d</span><span><i style="background:var(--gold)"></i>1x legal</span></div>
    <svg width="217" height="120" viewBox="0 0 217 120" role="img" aria-label="Donut chart: marketing 12%, sg&amp;a 21%, r&amp;d 60%, legal 7%">
      <g transform="translate(108,62) rotate(-90)" fill="none" stroke-width="24">
        <circle r="42" stroke="var(--sky)" stroke-dasharray="31.7 232.2"/>
        <circle r="42" stroke="var(--orange)" stroke-dasharray="55.4 208.5" stroke-dashoffset="-31.7"/>
        <circle r="42" stroke="var(--grey)" stroke-dasharray="158.3 105.6" stroke-dashoffset="-87.1"/>
        <circle r="42" stroke="var(--gold)" stroke-dasharray="18.5 245.4" stroke-dashoffset="-245.4"/>
      </g>
      <g font-size="4.5" fill="#fff" text-anchor="middle">
        <text x="124" y="22">marketing</text><text x="124" y="27">12%</text>
        <text x="149" y="54">sg&amp;a</text><text x="149" y="59">21%</text>
        <text x="77" y="89">r&amp;d</text><text x="77" y="94">60%</text>
        <text x="99" y="20">legal</text><text x="99" y="25">7%</text>
      </g>
    </svg>
    <p class="tx just" style="margin-top:8px">Lorem Ipsum is simply dummy text of the printing and typesetting industry. Lorem Ipsum has been the industry's standard dummy text ever since the 1500s, when an unknown printer took a galley of type and scrambled it to make a type specimen book. It has survived not only five centuries, but also the leap into electronic typesetting, remaining essentially unchanged. It was popularised in the 1960s with the release of Typeline sheets containing Lorem Ipsum passages, and more recently with desktop publishing software like Folio Layout including versions of Lorem Ipsum.</p>
    <p class="tx just">It is a long established fact that a reader will be distracted by the readable content of a page when looking at its layout. The point of using Lorem Ipsum is that it has a more-or-less normal distribution of letters, as opposed to using 'Content here, content here', making it look like readable English.</p>
  </div>
  <footer class="foot"><span class="mark">KESTREL</span><span class="num">3</span></footer>
</section>

<section class="page c3 r2">
  <h2 class="page-title">PUT HEADLINE <b>CONTENTS</b></h2>
  <div class="body">
    <h3 class="h3" style="margin-top:0">Implementation Estimate</h3>
    <p class="tx">The bulk of the implementation costs will be defined by discovery. Based on similar CRM implementation projects, we feel the CRM side will be somewhere between 200 and 300 hours, give or take. The wide swing in hours in phase one is related to the integration project. Our focus in discovery will be to nail down those requirements and our role as it relates to what is needed to integrate the sites with the CRM.</p>
    <table class="grid" style="margin-top:6px"><tr><td></td><td></td><td></td></tr><tr><td></td><td></td><td></td></tr><tr><td></td><td></td><td></td></tr><tr><td></td><td></td><td></td></tr><tr><td></td><td></td><td></td></tr><tr><td></td><td></td><td></td></tr></table>
    <table class="grid light" style="margin-top:18px"><tr><td></td><td></td><td></td><td></td><td></td></tr><tr><td></td><td></td><td></td><td></td><td></td></tr><tr><td></td><td></td><td></td><td></td><td></td></tr><tr><td></td><td></td><td></td><td></td><td></td></tr><tr><td></td><td></td><td></td><td></td><td></td></tr><tr><td></td><td></td><td></td><td></td><td></td></tr></table>
    <h3 class="h3" style="margin-top:18px">Implementation Estimate</h3>
    <p class="tx">The bulk of the implementation costs will be defined by discovery. Based on similar CRM implementation projects, we feel the CRM side will be somewhere between 200 and 300 hours, give or take. Our role as it relates to what is needed to integrate the sites with the CRM.</p>
  </div>
  <footer class="foot"><span class="mark">KESTREL</span><span class="num">3</span></footer>
</section>

<section class="page c4 r2">
  <h2 class="page-title">PUT HEADLINE <b>CONTENTS</b></h2>
  <div class="body">
    <h3 class="h3" style="margin-top:0">Implementation Estimate</h3>
    <p class="tx">The bulk of the implementation costs will be defined by discovery. Based on similar CRM implementation projects, we feel the CRM side will be somewhere between 200 and 300 hours, give or take. The wide swing in hours in phase one is related to the integration project. Our focus in discovery will be to nail down those requirements and our role as it relates to what is needed to integrate the sites with the CRM.</p>
    <table class="est">
      <tr><th style="width:60%">Task</th><th>Hours</th><th>Cost</th></tr>
      <tr><td>Discovery</td><td class="n">40</td><td class="n">$8,000</td></tr>
      <tr class="ph"><td>Phase 1</td><td></td><td></td></tr>
      <tr><td>Discovery</td><td class="n">20-40</td><td class="n">$8,000</td></tr>
      <tr><td>Discovery</td><td class="n">20-40</td><td class="n">$8,000</td></tr>
      <tr><td>Discovery</td><td class="n">20-40</td><td class="n">$8,000</td></tr>
      <tr class="tot"><td>Total Phase 1</td><td class="n">80-240</td><td class="n">$16,800-40,000</td></tr>
      <tr class="ph"><td>Phase 2</td><td></td><td></td></tr>
      <tr><td>Discovery</td><td class="n">20-40</td><td class="n">$8,000</td></tr>
      <tr class="tot"><td>Total Phase 2</td><td class="n">80-240</td><td class="n">$16,800-40,000</td></tr>
      <tr class="grand"><td>Total Estimated Implementation Cost</td><td class="n">220-480</td><td class="n">$44,000-96,000</td></tr>
    </table>
    <h3 class="h3" style="margin-top:10px">Project Timeline</h3>
    <p class="tx">Based on the information we have at our disposal, the launch date doesn't seem a realistic goal to get both the work done needed to provide the foundation for the future CRM instance and the integration given the state of flux of the requirements. We are currently estimating that the first phase will take between 7 and 12 weeks.</p>
    <table class="est">
      <tr><th style="width:60%">Task</th><th>Weeks to Complete</th></tr>
      <tr><td>Discovery</td><td class="n">1-2</td></tr>
      <tr><td>Phase 1</td><td class="n">6-10</td></tr>
      <tr><td>Phase 2</td><td class="n">8-12</td></tr>
      <tr class="tot"><td>Total Number of Weeks</td><td class="n"></td></tr>
    </table>
  </div>
  <footer class="foot"><span class="mark">KESTREL</span><span class="num">3</span></footer>
</section>

<section class="page c1 r3">
  <h2 class="page-title">PUT HEADLINE <b>CONTENTS</b></h2>
  <div class="photo" role="img" aria-label="Photo of a team working together around a table"></div>
  <div class="body" style="top:148px">
    <p class="mission">Ledgerly's mission is to help and support the self-employed and small business owners with</p>
    <p class="tx">Administrative tasks are cumbersome, time-consuming and often prevent small owners from focusing their time and energy on their business and their customers. They can also be extremely stressful for first timers.</p>
    <p class="tx">At Ledgerly, we envisage accounting for the self-employed and small business owners as being <a>automated and decentralized</a></p>
    <div class="bar"></div><div class="bar"></div><div class="bar"></div>
    <p class="tx">Ledgerly is based on an innovative license model that uses Token-as-a-License (TaaL). The token represents lifelong software license for Ledgerly solutions. The token sales will enable Ledgerly to deliver fully automatic bookkeeping.</p>
  </div>
  <footer class="foot"><span class="mark">KESTREL</span><span class="num">3</span></footer>
</section>

<section class="page c2 r3">
  <div class="back-band">
    <svg width="269" height="250" aria-hidden="true"><polygon points="60,0 269,0 269,130 175,250" fill="var(--navy-light)" opacity=".6"/><polygon points="0,0 60,0 175,250 0,250" fill="var(--navy-deep)" opacity=".5"/></svg>
  </div>
  <div class="back-brand">KESTREL ADVISORS</div>
  <div class="contacts">
    <div>P: +00 555 010 2040<br>F: +00 555 010 3050</div>
    <div>hello@kestreladvisors.example<br>www.kestreladvisors.example</div>
    <div>P.O. Box 4410, Northvale<br>Tel: 555 0199</div>
  </div>
</section>

</body>
</html>
```